Business Card Design

Carl Benson Insurance Agency, an Independent Insurance Agency which was stated on Orchard Lane in Laplace, Louisiana on 1958 and has grown the six locations throughout South Louisiana. We sell personal (auto Homeowners flood, liability) and commercial insurance (commercial property, general liability, workers compensation, commercial auto). I am looking for a double sided card with list the five remaining locations on the back or maybe even a folded four sided card. Our home office is a two story building with a green roof. I have had a logo designed which I have attached. Open for revisions but would like to stay with in the same green roof over an M. I have attached the logo but can not tell if I was uploaded.

Target Market(s)

Individual and commercial insurance buyers. Upper income and business owners

Industry/Entity Type

Insurance

Requirements
Must have
• Must have similar logo as uploaded. Green roof over M or something similar. List all location address and phone numbers.

Employee name, office phone number; direct phone line; email address and website list all locations on card. Very Similar colors to current logo.
Nice to have
• Possible folded card with double sided print

```html
<!DOCTYPE html>
<html lang="en">
<head>
<meta charset="utf-8">
<title>Carl Benson Insurance Agency – Stationery</title>
<link rel="stylesheet" href="https://fonts.googleapis.com/css2?family=Arimo:ital,wght@0,400;0,700;1,400;1,700&display=swap">
<style>
  :root{
    --backdrop:#8e8e8e;
    --paper:#ffffff;
    --brand-blue:#1a78c2;
    --brand-green:#1d5b2c;
    --folder-top:#0ea0e2;
    --folder-bottom:#0a6fc3;
    --ink:#444444;
    --muted:#5a5a5a;
    --rule:#1a78c2;
    --mark-light:rgba(26,120,194,.06);
    --mark-white:rgba(255,255,255,.10);
  }
  *{box-sizing:border-box;margin:0;padding:0}
  html,body{width:1191px;height:1200px;overflow:hidden}
  body{background:var(--backdrop);font-family:"Arimo",Arial,sans-serif;color:var(--ink);position:relative}
  .sheet{position:absolute;background:var(--paper);box-shadow:0 1px 4px rgba(0,0,0,.35);overflow:hidden}
  .watermark{position:absolute;background:var(--mark-light)}
  .card--blue .watermark,.folder .watermark{background:var(--mark-white)}
  .brand{position:absolute;display:flex;align-items:center;gap:7px;font-weight:700;color:var(--brand-green);text-transform:uppercase;line-height:1.05;white-space:nowrap}
  .brand-square{width:22px;height:22px;background:var(--brand-green);flex:none}
  .brand-name{font-size:15px;letter-spacing:.2px}
  .brand--white{color:#fff}
  .brand--white .brand-square{background:#fff}

  /* Fax sheet */
  .fax{left:49px;top:41px;width:490px;height:632px}
  .fax .brand{left:164px;top:34px}
  .fax-title{position:absolute;left:0;right:0;top:88px;text-align:center;font-size:14px;font-weight:700;font-style:italic;color:var(--brand-blue)}
  .fax-table{position:absolute;left:31px;top:116px;width:428px;border-top:1px dashed var(--rule);border-bottom:1px dashed var(--rule)}
  .fax-row{display:grid;grid-template-columns:44px 164px 44px 1fr;font-size:9.5px;height:18px;align-items:center}
  .fax-row:first-child{border-bottom:1px dashed var(--rule)}
  .fax-row b{color:var(--brand-blue);font-weight:700}
  .fax-row i{font-style:italic;color:var(--muted)}
  .fax-section{position:absolute;left:35px;width:440px;display:grid;grid-template-columns:90px 1fr;font-size:9.5px;line-height:14px}
  .fax-section b{color:var(--brand-blue)}
  .fax-section p{color:var(--muted)}

  /* contact footer */
  .contact-list{position:absolute;font-size:9.5px;line-height:13px;color:var(--muted)}
  .contact-list li{list-style:none;display:flex;align-items:center;gap:6px}
  .icon{width:10px;height:10px;fill:var(--brand-blue);flex:none}
  .divider{position:absolute;width:1px;background:var(--brand-blue)}
  .contact-web{position:absolute;font-size:9.5px;color:var(--muted);display:flex;align-items:center;gap:6px}

  /* Letterhead */
  .letter{left:293px;top:247px;width:489px;height:630px}
  .letter .brand{left:165px;top:33px}
  .letter-body{position:absolute;left:52px;top:123px;width:420px;font-size:7.4px;line-height:10.4px;color:var(--ink)}
  .letter-body p{margin-bottom:9px}
  .signature{width:120px;height:36px;margin-top:6px;background:linear-gradient(90deg,rgba(26,120,194,.12),rgba(26,120,194,.05));border-radius:3px}
  .letter-address{position:absolute;right:27px;top:565px;font-size:9.5px;line-height:13px;text-align:right;color:var(--muted);white-space:nowrap;font-style:normal}
  .letter-address b{font-weight:400;color:var(--brand-blue)}

  /* Folder */
  .folder{left:653px;top:108px;width:490px;height:632px;background:linear-gradient(180deg,var(--folder-top),var(--folder-bottom))}
  .folder .brand{left:126px;top:90px;gap:10px}
  .folder .brand-square{width:44px;height:44px}
  .folder .brand-name{font-size:22px}
  .folder-credit{position:absolute;left:0;right:0;top:522px;text-align:center;color:#fff;text-transform:uppercase}
  .folder-credit .lead{font-size:15px;letter-spacing:.5px}
  .folder-credit .person{font-size:23px;font-weight:700;margin-top:4px}
  .folder-credit .agency{font-size:13.5px;margin-top:2px}

  /* Cards */
  .card{top:952px;width:261px;height:147px}
  .card--front{left:171px}
  .card--front .brand{left:22px;top:62px;gap:5px}
  .card .brand-square{width:16px;height:16px}
  .card .brand-name{font-size:9.5px}
  .card-name{position:absolute;left:148px;top:29px;font-size:8px;font-weight:700;color:var(--brand-blue)}
  .card-details{position:absolute;left:148px;top:49px;font-size:5.5px;line-height:7.5px;color:var(--muted)}
  .card-details li{list-style:none;display:flex;gap:4px;align-items:center}
  .card-details .icon{width:6px;height:6px}
  .card-details .gap{height:5px}
  .card--blue{background:linear-gradient(180deg,var(--folder-top),var(--folder-bottom))}
  .card--back{left:465px}
  .card--back2{left:759px}
  .card--back .brand{left:22px;top:104px;gap:5px}
  .card--back2 .brand{left:22px;top:20px;gap:5px}
  .card-web{position:absolute;font-size:6px;color:#fff;letter-spacing:.3px}
  .card--back .card-web{left:159px;top:120px}
  .card--back2 .card-web{left:22px;top:122px}
  .locations{position:absolute;left:22px;top:54px;width:220px;display:grid;grid-template-columns:1fr 1fr;column-gap:12px;row-gap:4px;color:#fff;font-size:5.5px;line-height:6.6px;list-style:none}
  .locations b{font-weight:700;display:block}
</style>
</head>
<body>

<!-- Fax transmittal -->
<section class="sheet fax">
  <div class="watermark" style="left:205px;top:500px;width:60px;height:132px"></div>
  <div class="brand"><span class="brand-square"></span><span class="brand-name">Carl Benson<br>Insurance Agency</span></div>
  <h1 class="fax-title">Facsimile Transmittal</h1>
  <div class="fax-table">
    <div class="fax-row"><b>Subject</b><i>: Your subject should be here</i><b>Date</b><i>: 25/01/2015</i></div>
    <div class="fax-row"><b>To</b><i>: Customer Company/Name Here</i><b>From</b><i>: Carl Benson Insurance Agency</i></div>
    <div class="fax-row"><b>Cc</b><i>: Customer Company/Name Here</i><b>Phone</b><i>: 985-555-0161</i></div>
    <div class="fax-row"><b>Fax</b><i>: Type Fax Number</i><b>Fax</b><i>: 985-555-0161</i></div>
  </div>
  <div class="fax-section" style="top:227px"><b>Action Required :</b><p>Lorem ipsum dolor sit amet, consectetuer adipiscing elit, sed diam non ummy nibh euismod tincidunt ut laoreet dolore.</p></div>
  <div class="fax-section" style="top:266px"><b>Recomendation :</b><p>Lorem ipsum dolor sit amet, consectetuer adipiscing elit, sed diam non ummy nibh euismod tincidunt ut laoreet dolore magna. Ut wisi enim ad minim veniam, quis nostrud.</p></div>
  <div class="fax-section" style="top:316px"><b>Background :</b><p>Lorem ipsum dolor sit amet, consectetuer adipiscing elit, sed diam non ummy nibh euismod tincidunt ut laoreet dolore magna. Ut wisi enim ad minim veniam, quis nostrud exerci tation ullamcorper suscipit lobortis nisl ut aliquip ex ea commodo consequat. Duis autem vel eum iriure dolor in hendrerit in vulputate velit esse molestie consequat, vel illum dolore eu feugiat nulla facilisis at vero eros et accumsan et iusto odio dignissim qui blandit praesent luptatum zzril delenit augue duis dolore te feugait nulla facilisi. Nam liber tempor cum soluta nobis eleifend option congue nihil imperdiet doming id quod mazim placerat facer possim assum. Typi non habent claritatem insitam; est usus legentis in iis qui facit eorum claritatem. Investigationes demonstraverunt lectores legere me lius quod ii legunt saepius. Claritas est etiam processus dynamicus, qui sequitur mutationem consuetudium lectorum. Mirum est notare.</p></div>
  <div class="fax-section" style="top:502px"><b>Background :</b><p>Lorem ipsum, dolor sit amet consectetuer adipiscing elit.</p></div>
  <ul class="contact-list" style="left:27px;top:567px">
    <li><svg class="icon" viewBox="0 0 10 10"><path d="M1 3c0-1 1-2 4-2s4 1 4 2v1H7V3H3v1H1z M2 5h6l1 4H1z"/></svg>225-555-0130 (Direct)</li>
    <li><svg class="icon" viewBox="0 0 10 10"><path d="M2 1l2 0 1 2-1 1c1 2 2 3 3 3l1-1 2 1v2c-5 0-8-3-8-8z"/></svg>985-555-0161 (Office)</li>
    <li><svg class="icon" viewBox="0 0 10 10"><path d="M0 2h10v6H0z M0 2l5 4 5-4" fill="none" stroke="#1a78c2"/></svg>nora.vance@carlbenson.com</li>
  </ul>
  <span class="divider" style="left:178px;top:566px;height:40px"></span>
  <span class="contact-web" style="left:191px;top:580px"><svg class="icon" viewBox="0 0 10 10"><circle cx="5" cy="5" r="4.3" fill="none" stroke="#1a78c2"/><path d="M0.7 5h8.6M5 0.7v8.6" stroke="#1a78c2" fill="none"/></svg>www.carlbenson.com</span>
</section>

<!-- Letterhead -->
<section class="sheet letter">
  <div class="watermark" style="left:215px;top:440px;width:210px;height:190px"></div>
  <div class="brand"><span class="brand-square"></span><span class="brand-name">Carl Benson<br>Insurance Agency</span></div>
  <div class="letter-body">
    <p>Dear Paul,</p>
    <p>Lorem ipsum dolor sit amet, consectetuer adipiscing elit, sed diam nonummy nibh euismod tincidunt ut laoreet dolore magna aliquam erat volutpat. Ut wisi enim ad minim veniam, quis nostrud exerci tation ullamcorper suscipit lobortis nisl ut aliquip ex ea commodo consequat. Duis dolore te feugait nulla facilisi. Nam liber tempor cum soluta nobis eleifend option congue nihil imperdiet doming id quod mazim placerat facer possim assum.</p>
    <p>Duis autem vel eum iriure dolor in hendrerit in vulputate velit esse molestie consequat, vel illum dolore eu feugiat nulla facilisis at vero eros et accumsan et iusto odio dignissim qui blandit praesent luptatum zzril delenit augue duis dolore te feugait nulla facilisi. Consectetuer adipiscing elit, sed diam nonummy nibh euismod tincidunt ut laoreet dolore magna aliquam erat volutpat. Ut wisi enim ad minim veniam, quis nostrud exerci tation ullamcorper suscipit lobortis nisl ut aliquip ex ea commodo consequat.</p>
    <p>Consectetuer adipiscing elit, sed diam nonummy nibh euismod tincidunt ut laoreet dolore magna aliquam erat volutpat. Ut wisi enim ad minim veniam, quis nostrud exerci tation ullamcorper suscipit lobortis nisl ut aliquip ex ea commodo consequat. Consectetuer adipiscing elit, sed diam nonummy nibh euismod tincidunt ut laoreet dolore magna aliquam erat volutpat. Ut wisi enim ad minim veniam, quis nostrud exerci tation ullamcorper suscipit lobortis nisl ut aliquip ex ea commodo consequat.</p>
    <p>Dolor sit amet, consectetuer adipiscing elit, sed diam nonummy nibh euismod tincidunt ut laoreet dolore magna aliquam erat volutpat. Ut wisi enim ad minim veniam, quis nostrud exerci tation ullamcorper suscipit lobortis nisl ut aliquip ex ea commodo consequat. Duis dolore te feugait nulla facilisi. Nam liber tempor cum soluta nobis eleifend option congue nihil imperdiet doming id quod mazim placerat facer possim assum. Duis dolore te feugait nulla facilisi. Nam liber tempor cum soluta nobis eleifend option congue nihil imperdiet doming id quod mazim placerat facer possim assum.Duis dolore te feugait nulla facilisi. Nam liber tempor cum soluta nobis eleifend option congue nihil imperdiet doming id quod mazim placerat facer possim assum.</p>
    <p>Sincerely,</p>
    <div class="signature" role="img" aria-label="Handwritten signature of the sender"></div>
  </div>
  <ul class="contact-list" style="left:29px;top:565px">
    <li><svg class="icon" viewBox="0 0 10 10"><path d="M1 3c0-1 1-2 4-2s4 1 4 2v1H7V3H3v1H1z M2 5h6l1 4H1z"/></svg>225-555-0130 (Direct)</li>
    <li><svg class="icon" viewBox="0 0 10 10"><path d="M2 1l2 0 1 2-1 1c1 2 2 3 3 3l1-1 2 1v2c-5 0-8-3-8-8z"/></svg>985-555-0161 (Office)</li>
    <li><svg class="icon" viewBox="0 0 10 10"><path d="M0 2h10v6H0z M0 2l5 4 5-4" fill="none" stroke="#1a78c2"/></svg>nora.vance@carlbenson.com</li>
  </ul>
  <span class="divider" style="left:178px;top:563px;height:40px"></span>
  <span class="contact-web" style="left:190px;top:579px"><svg class="icon" viewBox="0 0 10 10"><circle cx="5" cy="5" r="4.3" fill="none" stroke="#1a78c2"/><path d="M0.7 5h8.6M5 0.7v8.6" stroke="#1a78c2" fill="none"/></svg>www.carlbenson.com</span>
  <span class="divider" style="left:314px;top:563px;height:40px"></span>
  <address class="letter-address"><b>Carl Benson Insurance Agency</b><br>410 West Magnolia<br>Suite 3 Hammond, LA 70401</address>
</section>

<!-- Presentation folder -->
<section class="sheet folder">
  <div class="brand brand--white"><span class="brand-square"></span><span class="brand-name">Carl Benson<br>Insurance Agency</span></div>
  <div class="folder-credit">
    <p class="lead">Directed by</p>
    <p class="person">Nora Vance</p>
    <p class="agency">Carl Benson Insurance Agency</p>
  </div>
</section>

<!-- Business card front -->
<section class="sheet card card--front">
  <div class="brand"><span class="brand-square"></span><span class="brand-name">Carl Benson<br>Insurance Agency</span></div>
  <p class="card-name">NORA VANCE</p>
  <ul class="card-details">
    <li><svg class="icon" viewBox="0 0 10 10"><path d="M5 0a3.5 3.5 0 0 1 3.5 3.5C8.5 6 5 10 5 10S1.5 6 1.5 3.5A3.5 3.5 0 0 1 5 0z"/></svg><span style="color:#1a78c2">Carl Benson Insurance Agency</span></li>
    <li style="padding-left:10px">410 West Magnolia</li>
    <li style="padding-left:10px">Suite 3 Hammond, LA 70401</li>
    <li class="gap"></li>
    <li><svg class="icon" viewBox="0 0 10 10"><path d="M1 3c0-1 1-2 4-2s4 1 4 2v1H7V3H3v1H1z M2 5h6l1 4H1z"/></svg>225-555-0130 (Direct)</li>
    <li><svg class="icon" viewBox="0 0 10 10"><path d="M2 1l2 0 1 2-1 1c1 2 2 3 3 3l1-1 2 1v2c-5 0-8-3-8-8z"/></svg>985-555-0161 (Office)</li>
    <li><svg class="icon" viewBox="0 0 10 10"><path d="M0 2h10v6H0z"/></svg>nora.vance@carlbenson.com</li>
    <li><svg class="icon" viewBox="0 0 10 10"><circle cx="5" cy="5" r="5"/></svg>www.carlbenson.com</li>
  </ul>
</section>

<!-- Business card back -->
<section class="sheet card card--blue card--back">
  <div class="watermark" style="left:160px;top:0;width:80px;height:147px"></div>
  <div class="brand brand--white"><span class="brand-square"></span><span class="brand-name">Carl Benson<br>Insurance Agency</span></div>
  <p class="card-web">www.carlbenson.com</p>
</section>

<!-- Business card locations side -->
<section class="sheet card card--blue card--back2">
  <div class="watermark" style="left:160px;top:0;width:80px;height:147px"></div>
  <div class="brand brand--white"><span class="brand-square"></span><span class="brand-name">Carl Benson<br>Insurance Agency</span></div>
  <ul class="locations">
    <li><b>LaPlace (Home Office)</b>120 Orchard Lane · 985-555-0101</li>
    <li><b>Hammond</b>410 West Magnolia · 985-555-0161</li>
    <li><b>Gonzales</b>88 Cedar Row · 225-555-0144</li>
    <li><b>Houma</b>215 Bayou Park Dr · 985-555-0172</li>
    <li><b>Thibodaux</b>56 Canal Bend · 985-555-0188</li>
    <li><b>Covington</b>302 Pine Crest Rd · 985-555-0195</li>
  </ul>
  <p class="card-web">www.carlbenson.com</p>
</section>

</body>
</html>
```